Business Card Design

We are a commercial real estate brokerage in San Francisco, leasing office buildings downtown.
I would like a clean, elegant look. Simple but powerful .

Industry/Entity Type

Business

Contact Information for Business Card

Colin Farrow
lic# 07281549
415.555.0172
colin@tarvo-commercial.example
tarvo-commercial.example

```html
<!DOCTYPE html>
<html lang="en">
<head>
<meta charset="utf-8">
<title>Tarvo Commercial — Business Card</title>
<link href="https://fonts.googleapis.com/css2?family=Source+Sans+3:wght@400;600&display=swap" rel="stylesheet">
<style>
  :root {
    --stage: #000000;
    --card: #ffffff;
    --accent: #6f7fa0;
    --ink: #444444;
    --mark: #5a5a5a;
    --emboss: #e4e4e4;
  }
  * { margin: 0; padding: 0; box-sizing: border-box; }
  html, body {
    width: 960px; height: 1200px; overflow: hidden;
    background: var(--stage);
    font-family: "Source Sans 3", sans-serif;
  }
  .card {
    position: absolute; left: 193px; width: 574px; height: 337px;
    background: var(--card);
  }
  .card--front { top: 251px; }
  .card--back { top: 623px; }

  .brand { position: absolute; display: flex; align-items: center; }
  .brand__square { background: var(--mark); flex: none; }
  .brand__name { font-weight: 600; white-space: nowrap; }

  .card--front .brand { left: 34px; top: 148px; width: 222px; gap: 10px; }
  .card--front .brand__square { width: 34px; height: 34px; }
  .card--front .brand__name { font-size: 21px; color: var(--accent); }

  .card--back .brand { left: 0; right: 0; top: 136px; justify-content: center; gap: 22px; }
  .card--back .brand__square { width: 64px; height: 64px; background: var(--emboss); }
  .card--back .brand__name { font-size: 52px; color: var(--emboss); font-weight: 400; }

  .contact { position: absolute; left: 286px; top: 94px; color: var(--ink); }
  .contact__name { font-size: 20px; font-weight: 600; color: var(--accent); line-height: 26px; }
  .contact__licence { font-size: 16px; margin-top: 20px; line-height: 20px; }
  .contact__list { list-style: none; margin-top: 18px; }
  .contact__item {
    display: flex; align-items: center; gap: 6px;
    font-size: 16px; line-height: 21px;
  }
  .contact__icon { width: 11px; height: 11px; fill: var(--accent); flex: none; }
</style>
</head>
<body>
  <section class="card card--front">
    <div class="brand">
      <span class="brand__square"></span>
      <span class="brand__name">Tarvo Commercial</span>
    </div>
    <div class="contact">
      <p class="contact__name">Colin Farrow</p>
      <p class="contact__licence">Lic# 07281549</p>
      <ul class="contact__list">
        <li class="contact__item">
          <svg class="contact__icon" viewBox="0 0 24 24" aria-hidden="true"><path d="M6.6 10.8a15 15 0 0 0 6.6 6.6l2.2-2.2c.3-.3.7-.4 1-.2 1.1.4 2.3.6 3.6.6.6 0 1 .4 1 1V20c0 .6-.4 1-1 1A17 17 0 0 1 3 4c0-.6.4-1 1-1h3.5c.6 0 1 .4 1 1 0 1.3.2 2.5.6 3.6.1.3 0 .7-.2 1z"/></svg>
          415.555.0172
        </li>
        <li class="contact__item">
          <svg class="contact__icon" viewBox="0 0 24 24" aria-hidden="true"><path d="M2 5h20v14H2zm2 2v.3l8 5.5 8-5.5V7l-8 5.4z"/></svg>
          colin@tarvo-commercial.example
        </li>
        <li class="contact__item">
          <svg class="contact__icon" viewBox="0 0 24 24" aria-hidden="true"><circle cx="12" cy="12" r="9.5" fill="none" stroke="#6f7fa0" stroke-width="2"/><path d="M2.5 12h19M12 2.5c-5 5-5 14 0 19M12 2.5c5 5 5 14 0 19M4.5 7h15M4.5 17h15" fill="none" stroke="#6f7fa0" stroke-width="1.6"/></svg>
          tarvo-commercial.example
        </li>
      </ul>
    </div>
  </section>

  <section class="card card--back">
    <div class="brand">
      <span class="brand__square"></span>
      <span class="brand__name">Tarvo Commercial</span>
    </div>
  </section>
</body>
</html>
```